Crintle Homes from US$9,995– Making buying a house as easy as ordering a pizza online - worldwide

I am after a website that is fun and interactive.

Buying a house should be as simple as buying a Pizza delivery online.....

Margherita 20' ………………………………………….US$9,995
Standard, 30sqm Studio with kitchen & Bathroom, Flat Roof
Four Cheese 20' ………………………………………….US$11,995
Standard, 30sqm Studio with kitchen & Bathroom, Pitched Roof
Supreme 40' ………………………………………….US$18,995
Standard, 60sqm, 2 Bedrooms, Lounge, kitchen & Bathroom, Flat Roof
Pepperoni 40' ………………………………………….US$20,995
Standard, 60sqm, 2 Bedrooms, Lounge, kitchen & Bathroom, Pitched Roof
Hawaiian 40' ………………………………………….US$22,995
Beach design, 60sqm, 2 Bedrooms, Lounge, kitchen & Bathroom, Pitched Roof
The Works 40' ………………………………………….US$24,995
Beach design, 60sqm, 2 Bedrooms, Lounge, kitchen, Bathroom, Deck, Pitched Roof

eg. https://www.dishorbit.com.au/ https://www.crustvane.com

I want a fun design....

i want to reinvent how people DESIGN - BUILD and DELIVER housing

I want a SaaS solution for drop shipping pre-built houses.

The main campaign, we are offering 1,000 homes (to anywhere in the world) for US$9,995 + shipping

Just need to Pay a Fully refundable $100 Deposit to pre-register (so need a shopping cart & payment solution).

"Queue Jumper" - pay in full and jump the queue to get your Crintle months earlier.

The campaign is based on crowdsourcing - we need 1000 participants to pre-register - then everyone's orders will be filled .

The design is very simple...
HEADER
- The Story
- The Product
- Design our Own
- Pre-Register
- Contact Us

- Login
- Shopping Cart

FOOTER
- Privacy
- Terms & Conditions
- Investment
- Media
- NGO/Government
- Contact
- Sitemap

The important parts is that everyone who
- Subscribes
- Makes Contact
- Pre-registers
…in the system automatically gets an account (just need name and email address).
The user is then sent an email with details on how they can log back in at any time and see purchases, update profile (eg. Shipping address, contact details, etc....)

This data also needs to be sent to a CRM eg Leadmoor for marketing to automate regular updates to all users.

It also needs to link to Facebook, LinkedIn , TikTok, Instagram, Twitter

You can get sample content from our old website https://tenvaledwellings.webplotter.com/ - Plus I have attached updated content in this Brief.

The hero image should be a slider with videos and images with links to "Call to Action"

PLEASE NOTE: that "crintle" is a brand new product that we pre build offsite so when it is delivered, it is ready to move in to. So we need a whole new look and a new style

This is a wordpress site to be hosted on my server - Once completed I need full access to add, amend and update any pages, images products

I am very open to different colours - do not be limited by the colours in the logo.

I would be interested to see what you can do with NO white backgrounds. (This might look good or could look horrible)

And most importantly what will your design look like on mobile devices (phones / ipads)

SUCCESS (1) is getting the user to LOOK - DREAM - BUY (Or at least pre-register)

SUCCESS (2) it MUST look fun but still highly professional and TRUSTWORTHY to get the interest of investors to invest millions $$$$$

SUCCESS (3) we need to get "Inflencers / Bloggers" talking about Crintle - this could be done by a campaign to get a million likes and get a FREE home fo both the follower and the blogger

Target Market(s)

New home buyers (younger demographic), Families wanting to extend (middle aged)

Industry/Entity Type

Housing, Crowdsourcing, Drop shipping, SaaS technology

Coding

Coded - Design and coding required

Colors
0054AA
0677BA
7BADD7
CADEEF
E8F1F8
EE7325
F08F49
F5BC92
FAE3D3
FDF4ED

Requirements
Must have
• ecommerce, user accounts, social media & crm connections for crowdsourcing marketing, Call to actions
Nice to have
• $1,000,000
Should not have
• Do NOT complicate the funnel in the steps to sign-up

```html
<!DOCTYPE html>
<html lang="en">
<head>
<meta charset="utf-8">
<title>Crintle Homes – Design Build Deliver</title>
<link href="https://fonts.googleapis.com/css2?family=Montserrat:ital,wght@0,400;0,500;0,600;0,700;0,800;1,400;1,700&display=swap" rel="stylesheet">
<style>
:root{
  --blue:#0054AA;
  --blue-mid:#0677BA;
  --orange:#EE7325;
  --orange-soft:#F08F49;
  --peach:#F5BC92;
  --dark:#2b2b2b;
  --darker:#1c1c1c;
  --white:#ffffff;
  --yellow:#f4f01a;
  --line:#cfcfcf;
}
*{box-sizing:border-box;margin:0;padding:0}
html,body{width:1200px;height:3668px;overflow:hidden}
body{font-family:'Montserrat',sans-serif;color:var(--white);background:var(--darker)}
.page{position:relative;width:1200px;height:3668px;overflow:hidden}
.abs{position:absolute}
.edge{position:absolute;left:0;width:1200px;height:40px}

/* hero */
.hero{position:absolute;left:0;top:0;width:1200px;height:720px;background:linear-gradient(180deg,#3a3a3a,#2e2e2e)}
.hero-wedge{position:absolute;left:0;top:0}
.brand{position:absolute;left:111px;top:26px;font-weight:800;font-size:46px;letter-spacing:1px;color:var(--white);line-height:1}
.nav{position:absolute;left:451px;top:74px;display:flex;gap:24px;font-size:17.5px;font-weight:600}
.login{position:absolute;left:964px;top:26px;font-size:18px;font-weight:600;display:flex;align-items:center;gap:4px}
.cart{position:absolute;left:1047px;top:16px;width:40px;height:40px;border-radius:50%;background:var(--orange);display:flex;align-items:center;justify-content:center}
.hero-title{position:absolute;left:107px;top:160px;font-weight:800;font-size:51px;line-height:59px}
.hero-title .hl{color:var(--yellow)}
.hero-lead{position:absolute;left:111px;top:352px;width:450px;font-size:18.5px;line-height:29px}
.contactless{position:absolute;left:114px;top:440px;font-size:19px;font-weight:700;font-style:italic}
.search{position:absolute;left:111px;top:481px;display:flex;height:63px}
.search-input{width:326px;background:var(--white);color:#666;font-size:16px;display:flex;align-items:center;padding-left:22px;gap:6px}
.search-btn{width:125px;background:var(--orange);font-weight:700;font-size:19px;display:flex;align-items:center;justify-content:center}
.watch{position:absolute;left:108px;top:567px;display:flex;align-items:center;gap:14px;font-weight:600;font-size:18px}
.watch-dot{width:62px;height:62px;border-radius:50%;background:var(--darker);display:flex;align-items:center;justify-content:center}
.price-badge{position:absolute;left:550px;top:157px;width:136px;height:136px;border-radius:50%;background:var(--darker);text-align:center;padding-top:32px}
.price-badge strong{display:block;font-size:31px;font-weight:800;border-bottom:2px solid var(--yellow);margin:0 22px 6px;padding-bottom:4px}
.price-badge span{font-size:17px}
.hero-house{position:absolute;left:576px;top:170px;width:624px;height:485px;background:linear-gradient(150deg,#e9e7e3,#b9b4ad);clip-path:polygon(55% 0,100% 30%,100% 62%,38% 100%,0 72%,0 40%)}
.slider-arrow{position:absolute;left:34px;top:330px}

/* story */
.story{position:absolute;left:0;top:715px;width:1200px;height:780px;background:var(--blue)}
.story-sketch{position:absolute;left:0;top:55px;width:570px;height:610px;background:linear-gradient(120deg,#0a4a93,#0a5cb3)}
.eyebrow{font-size:24px;font-weight:500}
.section-title{font-weight:800;font-size:48px;line-height:1.1}
.story-copy{position:absolute;left:564px;top:92px;width:545px}
.story-copy .section-title{margin-top:6px}
.story-copy p{font-size:16px;line-height:23px;margin-top:22px}
.ticks{list-style:none;margin-top:22px}
.ticks li{position:relative;padding-left:26px;font-size:16px;line-height:23px;margin-bottom:22px}
.ticks li::before{content:"";position:absolute;left:0;top:4px;width:14px;height:14px;border-radius:50%;background:var(--white)}
.ticks li::after{content:"";position:absolute;left:4px;top:7px;width:5px;height:3px;border-left:2px solid currentColor;border-bottom:2px solid currentColor;transform:rotate(-45deg)}
.story .ticks li::after{border-color:var(--blue)}
.btn{display:inline-flex;align-items:center;justify-content:center;background:var(--orange);color:var(--white);font-weight:600;text-transform:uppercase}
.read-more{position:absolute;left:565px;top:646px;width:148px;height:58px;font-size:18px}

/* properties */
.props{position:absolute;left:0;top:1495px;width:1200px;height:920px;background:linear-gradient(180deg,#2c2c2c,#3c3a38 50%,#2a2928)}
.props-head{position:absolute;left:0;top:90px;width:1200px;text-align:center}
.props-head .eyebrow{font-size:27px}
.props-head .section-title{font-weight:700;margin-top:10px}
.prop{position:absolute;width:434px}
.prop-top{display:flex;justify-content:space-between;font-weight:700;font-size:21px;padding-bottom:14px;border-bottom:3px solid var(--line)}
.prop p{font-size:16px;line-height:26px;margin-top:14px;padding-left:3px}
.order{position:absolute;left:456px;top:743px;width:220px;height:77px;font-size:24px}

/* register */
.reg{position:absolute;left:0;top:2405px;width:1200px;height:800px;background:var(--orange)}
.reg-copy{position:absolute;left:110px;top:92px;width:440px}
.reg .ticks li{font-size:16px;line-height:26px;margin-bottom:24px}
.reg .ticks li::after{border-color:var(--orange)}
.reg .ticks{margin-top:30px}
.reg-illus{position:absolute;left:0;top:421px;width:562px;height:390px;background:linear-gradient(160deg,#f5f3ef,#d9cfc0);clip-path:polygon(0 8%,45% 0,95% 12%,100% 100%,0 100%)}
.form{position:absolute;left:616px;top:86px;width:473px}
.field{height:49px;background:var(--white);color:#555;font-size:16px;display:flex;align-items:center;padding-left:17px;margin-bottom:15px;border:1px solid #ddd}
.choose{font-size:30px;font-weight:600;margin-top:28px}
.radio{position:relative;padding-left:29px;font-size:16px;line-height:26px;margin-top:14px}
.radio::before{content:"";position:absolute;left:0;top:5px;width:16px;height:16px;border:2px solid var(--white);border-radius:50%}
.note{font-size:13.5px;font-style:italic;line-height:19px;margin-top:20px}
.submit{display:inline-flex;margin-top:30px;width:123px;height:60px;background:var(--darker);font-weight:700;font-size:17px;align-items:center;justify-content:center}

/* footer */
.footer{position:absolute;left:0;top:3200px;width:1200px;height:468px;background:var(--darker)}
.footer .brand{top:100px;font-size:62px}
.f-col{position:absolute;top:82px}
.f-col h4{font-size:19px;font-weight:700;margin-bottom:18px}
.f-col a{display:block;color:var(--white);text-decoration:none;font-size:16.5px;line-height:28.5px}
.f-line{display:flex;gap:10px;font-size:16.5px;line-height:23px;margin-bottom:20px}
.f-line svg{flex:none;margin-top:4px}
.f-divider{position:absolute;left:111px;top:366px;width:978px;height:1px;background:#555}
.copy{position:absolute;left:111px;top:406px;font-size:16.5px}
.socials{position:absolute;left:834px;top:393px;display:flex;gap:6px}
.socials span{width:46px;height:46px;border-radius:50%;border:2px solid var(--orange)}
</style>
</head>
<body>
<div class="page">

  <!-- HERO -->
  <section class="hero">
    <svg class="hero-wedge" width="1200" height="720" aria-hidden="true"><polygon points="1200,0 1200,720 605,720" fill="#EE7325"/></svg>
    <div class="brand">CRINTLE</div>
    <nav class="nav"><span>The Story</span><span>The Product</span><span>Design our Own</span><span>Pre-Register</span><span>Contact Us</span></nav>
    <div class="login"><svg width="12" height="14" viewBox="0 0 12 14"><rect x="1" y="6" width="10" height="8" fill="#fff"/><path d="M3 6V4a3 3 0 0 1 6 0v2" stroke="#fff" stroke-width="2" fill="none"/></svg>Login</div>
    <div class="cart"><svg width="20" height="18" viewBox="0 0 20 18"><path d="M1 2h3l2 9h10l2-7H5" stroke="#fff" stroke-width="2" fill="none"/><circle cx="8" cy="15" r="1.6" fill="#fff"/><circle cx="15" cy="15" r="1.6" fill="#fff"/></svg></div>
    <svg class="slider-arrow" width="30" height="50" viewBox="0 0 30 50"><path d="M26 2L4 25l22 23" stroke="#9a9a9a" stroke-width="4" fill="none"/></svg>

    <h1 class="hero-title">DESIGN<br>BUILD<br><span class="hl">DELIVER</span></h1>
    <p class="hero-lead">Buying a house should be as simple as buying a Pizza delivery online.....</p>
    <p class="contactless">Contactless Delivery is now available!</p>
    <div class="search">
      <div class="search-input"><svg width="10" height="14" viewBox="0 0 10 14"><path d="M5 0a5 5 0 0 0-5 5c0 4 5 9 5 9s5-5 5-9a5 5 0 0 0-5-5z" fill="#666"/><circle cx="5" cy="5" r="2" fill="#fff"/></svg>Enter your Location for delivery</div>
      <div class="search-btn">SEARCH</div>
    </div>
    <div class="watch"><div class="watch-dot"><svg width="22" height="24" viewBox="0 0 22 24"><polygon points="2,0 22,12 2,24" fill="#fff"/></svg></div>WATCH VIDEO</div>

    <div class="hero-house" role="img" aria-label="3D cut-away model of a furnished prefab home with living room, kitchen and rooftop deck"></div>
    <div class="price-badge"><strong>$9,995</strong><span>+ shipping</span></div>
    <svg class="abs" style="left:672px;top:165px" width="200" height="130" viewBox="0 0 200 130" aria-hidden="true">
      <path d="M2 22 C40 0 60 20 55 30 C45 45 25 20 60 12 C110 0 120 80 190 100" stroke="#fff" stroke-width="4" fill="none"/>
      <path d="M170 82 L192 101 L168 113" stroke="#fff" stroke-width="4" fill="none"/>
    </svg>
  </section>

  <svg class="edge" style="top:690px" viewBox="0 0 1200 40" preserveAspectRatio="none" aria-hidden="true"><path fill="#0054AA" d="M0,40 L0,18 L40,10 L70,24 L100,6 L140,20 L170,12 L210,26 L240,8 L280,18 L320,4 L350,22 L390,12 L430,26 L460,10 L500,20 L540,6 L570,24 L610,14 L650,28 L680,8 L720,18 L760,4 L790,22 L830,12 L870,26 L900,10 L940,20 L980,6 L1010,24 L1050,14 L1090,28 L1120,8 L1160,18 L1200,10 L1200,40 Z"/></svg>

  <!-- STORY -->
  <section class="story">
    <div class="story-sketch" role="img" aria-label="Line sketch of a glass-walled interior with dining table and chairs"></div>
    <div class="story-copy">
      <div class="eyebrow">Our Team</div>
      <h2 class="section-title">THE STORY</h2>
      <p>Building a house should not be stressful – we believe it should be the happiest and one of the most rewarding experiences in your lifetime. So we set up our Happiness Brains Trust to troubleshoot how to remove the stress, delays and unexpected costs from building.</p>
      <p>The key problems our HBT came up with...and needed to solve:</p>
      <ul class="ticks">
        <li>Lack of tradesmen...and when you find them they can be VERY expensive.</li>
        <li>Lack of supply .... The waiting time on timber, widows, doors, etc is generally months or longer</li>
        <li>Lack of Communication – Getting all the tradies and suppliers to talk to each other and coordinate in a timely manner can be impossible and ends up costing months of delays.</li>
      </ul>
    </div>
    <div class="btn read-more">Read More</div>
  </section>

  <svg class="edge" style="top:1478px" viewBox="0 0 1200 40" preserveAspectRatio="none" aria-hidden="true"><path fill="#2c2c2c" d="M0,40 L0,18 L40,10 L70,24 L100,6 L140,20 L170,12 L210,26 L240,8 L280,18 L320,4 L350,22 L390,12 L430,26 L460,10 L500,20 L540,6 L570,24 L610,14 L650,28 L680,8 L720,18 L760,4 L790,22 L830,12 L870,26 L900,10 L940,20 L980,6 L1010,24 L1050,14 L1090,28 L1120,8 L1160,18 L1200,10 L1200,40 Z"/></svg>

  <!-- PROPERTIES -->
  <section class="props" role="img" aria-label="Dim interior of a finished home living room behind the property list">
    <div class="props-head">
      <div class="eyebrow">Projects</div>
      <h2 class="section-title">List Of Properties</h2>
    </div>
    <div class="prop" style="left:110px;top:250px"><div class="prop-top"><span>Margherita 20'</span><span>US$9,995</span></div><p>Standard, 30sqm Studio with kitchen &amp; Bathroom, Flat Roof</p></div>
    <div class="prop" style="left:652px;top:250px"><div class="prop-top"><span>Pepperoni 40</span><span>US$20,995</span></div><p>Standard, 60sqm, 2 Bedrooms, Lounge, kitchen &amp; Bathroom, Pitched Roof</p></div>
    <div class="prop" style="left:110px;top:412px"><div class="prop-top"><span>Four Cheese 20'</span><span>US$11,995</span></div><p>Standard, 30sqm Studio with kitchen &amp; Bathroom, Pitched Roof</p></div>
    <div class="prop" style="left:652px;top:412px"><div class="prop-top"><span>Hawaiian 40'</span><span>US$22,995</span></div><p>Beach design, 60sqm, 2 Bedrooms, Lounge, kitchen &amp; Bathroom, Pitched Roof</p></div>
    <div class="prop" style="left:110px;top:573px"><div class="prop-top"><span>Supreme 40'</span><span>US$18,995</span></div><p>Standard, 60sqm, 2 Bedrooms, Lounge, kitchen &amp; Bathroom, Flat Roof</p></div>
    <div class="prop" style="left:652px;top:573px"><div class="prop-top"><span>The Works 40'</span><span>US$24,995</span></div><p>Beach design, 60sqm, 2 Bedrooms, Lounge, kitchen, Bathroom, Deck, Pitched Roof</p></div>
    <div class="btn order">Order Now</div>
  </section>

  <svg class="edge" style="top:2385px" viewBox="0 0 1200 40" preserveAspectRatio="none" aria-hidden="true"><path fill="#EE7325" d="M0,40 L0,18 L40,10 L70,24 L100,6 L140,20 L170,12 L210,26 L240,8 L280,18 L320,4 L350,22 L390,12 L430,26 L460,10 L500,20 L540,6 L570,24 L610,14 L650,28 L680,8 L720,18 L760,4 L790,22 L830,12 L870,26 L900,10 L940,20 L980,6 L1010,24 L1050,14 L1090,28 L1120,8 L1160,18 L1200,10 L1200,40 Z"/></svg>

  <!-- PRE REGISTER -->
  <section class="reg">
    <div class="reg-copy">
      <div class="eyebrow">Register</div>
      <h2 class="section-title">PRE REGISTER</h2>
      <ul class="ticks">
        <li>To kickstart we are offering our first 1,000 houses for US$9,995</li>
        <li>All you need to do is give you name and email and you are registered.</li>
      </ul>
    </div>
    <div class="reg-illus" role="img" aria-label="3D render of a kitchen and lounge interior with sofa and dining chairs"></div>
    <form class="form">
      <div class="field">Full Name</div>
      <div class="field">Email</div>
      <div class="field">Phone Number</div>
      <div class="field">No of home do you want to reserve</div>
      <div class="choose">Choose one*</div>
      <div class="radio">In under 20 words tell us why you deserve to be one of the first 1,000 people in the world to get a Crintle home.</div>
      <div class="radio" style="margin-top:22px">Introduce 5 people to Crintle and get INSTANT approval.</div>
      <p class="note" style="margin-top:30px">You will be asked to pay a $100 refundable deposit.</p>
      <p class="note">When we give you a start date on the build, you will need to pay a 50% deposit. The balance is due once it is Quality tested and wrapped for shipping</p>
      <div class="submit">SUBMIT</div>
    </form>
  </section>

  <svg class="edge" style="top:3175px" viewBox="0 0 1200 40" preserveAspectRatio="none" aria-hidden="true"><path fill="#1c1c1c" d="M0,40 L0,18 L40,10 L70,24 L100,6 L140,20 L170,12 L210,26 L240,8 L280,18 L320,4 L350,22 L390,12 L430,26 L460,10 L500,20 L540,6 L570,24 L610,14 L650,28 L680,8 L720,18 L760,4 L790,22 L830,12 L870,26 L900,10 L940,20 L980,6 L1010,24 L1050,14 L1090,28 L1120,8 L1160,18 L1200,10 L1200,40 Z"/></svg>

  <!-- FOOTER -->
  <footer class="footer">
    <div class="brand">CRINTLE</div>
    <div class="f-col" style="left:549px">
      <h4>QUICK LINKS</h4>
      <a>Privacy</a><a>Terms &amp; Conditions</a><a>Investment</a><a>Media</a><a>NGO/Government</a><a>Contact</a><a>Sitemap</a>
    </div>
    <div class="f-col" style="left:807px">
      <h4>CONTACT US</h4>
      <div class="f-line"><svg width="10" height="14" viewBox="0 0 10 14"><path d="M5 0a5 5 0 0 0-5 5c0 4 5 9 5 9s5-5 5-9a5 5 0 0 0-5-5z" fill="#fff"/></svg><span>PO 512, Larkfield, Victoria 3267,<br>AUSTRALIA</span></div>
      <div class="f-line"><svg width="13" height="13" viewBox="0 0 13 13"><path d="M3 0l2 3-1.5 1.5a8 8 0 0 0 5 5L10 8l3 2-1.5 3C5 13 0 8 0 1.5z" fill="#fff"/></svg><span>040 555 218</span></div>
      <h4 style="margin-top:28px">HOURS</h4>
      <div class="f-line"><svg width="13" height="13" viewBox="0 0 13 13"><circle cx="6.5" cy="6.5" r="5.5" stroke="#fff" stroke-width="2" fill="none"/><path d="M6.5 3.5v3h2.5" stroke="#fff" stroke-width="1.6" fill="none"/></svg><span>Monday - Friday: 8am - 5pm<br>Saturday - Sunday: Closed</span></div>
    </div>
    <div class="f-divider"></div>
    <div class="copy">Copyright © 2022 Crintle - All Rights Reserved.</div>
    <div class="socials" aria-label="Social links"><span></span><span></span><span></span><span></span><span></span></div>
  </footer>
</div>
</body>
</html>
```